New Brand - Website Design (4 Pages)

We are launching a new brand for electronic cigarettes. We already have logo and packaging done and would like a web design to go with it.

We are interested in the following deliverables:

1) Home Page Design
2) Check Out Design
3) How it Works Page
4) Secondary Template Page Design

Looking for a 60s modern look and something that is consistent with our logo and packaging.

Industry/Entity Type

Electronic

Requirements
Must have
• Consistent with logo and packaging (Use Logo Attached)
White background

Example (Functionality & Design): http://www.torvex.co.uk/
Example (Design): http://www.quillharbor.com/

We want the design more like quillharbor but the functionality the same as torvex.

Top Bar: Pebble Arcs Kits; Cartridge Refills; How it Works; Contact; My Account; Checkout
Should not have
• Stock List or Search Bar or Newsletter Signup

```html
<!DOCTYPE html>
<html lang="en">
<head>
<meta charset="utf-8">
<title>How It Works – Pebble Arcs</title>
<link rel="stylesheet" href="https://fonts.googleapis.com/css2?family=Poiret+One&family=Carlito&family=Arimo:wght@400&display=swap">
<style>
  :root {
    --page: #ececec;
    --ink: #1a1a1a;
    --panel: #232323;
    --panel-text: #f2f2f2;
    --step-bg: #000000;
    --step-label: #333333;
    --body-grey: #5a5a5a;
    --heading-grey: #3a3a3a;
    --accent: #8fd3f1;
  }
  * { box-sizing: border-box; margin: 0; padding: 0; }
  html, body { width: 1200px; height: 1000px; overflow: hidden; }
  body { background: var(--page); color: var(--ink); position: relative; }

  .site-header { position: absolute; left: 0; top: 0; width: 1200px; height: 98px; }
  .brand-dot { position: absolute; left: 168px; top: 40px; width: 29px; height: 29px; border-radius: 50%; background: var(--accent); }
  .main-nav a {
    position: absolute; top: 49px; font-family: "Arimo", Arial, sans-serif; font-size: 10px;
    color: var(--ink); text-decoration: none; letter-spacing: 0.2px; white-space: nowrap;
  }
  .main-nav a.is-current::after {
    content: ""; position: absolute; left: -6px; right: -9px; top: 16px; height: 4px; background: var(--accent);
  }
  .brand { position: absolute; left: 902px; top: 24px; display: flex; align-items: center; gap: 8px; }
  .brand-mark { width: 50px; height: 50px; border-radius: 50%; background: var(--accent); }
  .brand-name { font-family: "Arimo", Arial, sans-serif; font-size: 13px; color: var(--ink); letter-spacing: 0.3px; line-height: 1; white-space: nowrap; }

  .intro {
    position: absolute; left: 164px; top: 98px; width: 875px; height: 219px;
    background: var(--panel); color: var(--panel-text); padding: 8px 10px 0 18px;
  }
  .intro h1 { font-family: "Poiret One", sans-serif; font-weight: 400; font-size: 38px; line-height: 46px; letter-spacing: 0.6px; }
  .intro p { font-family: "Carlito", Calibri, sans-serif; font-size: 18.5px; line-height: 24.8px; letter-spacing: 0.25px; white-space: nowrap; }

  .step { position: absolute; left: 164px; width: 874px; height: 296px; }
  .step-visual {
    position: absolute; top: 0; width: 437px; height: 296px; background: var(--step-bg);
    display: flex; align-items: center; justify-content: center; text-align: center;
    font-family: "Poiret One", sans-serif; font-size: 50px; line-height: 46px; letter-spacing: 1.5px; color: var(--step-label);
  }
  .step-copy { position: absolute; top: 0; width: 420px; }
  .step-copy h2 { font-family: "Poiret One", sans-serif; font-weight: 400; font-size: 28px; line-height: 34px; letter-spacing: 0.4px; color: var(--heading-grey); margin-top: 15px; }
  .step-copy p { font-family: "Poiret One", sans-serif; font-size: 18px; line-height: 24.7px; letter-spacing: 0.35px; color: var(--body-grey); margin-top: 22px; white-space: nowrap; }
  .step--image-left .step-visual { left: 0; }
  .step--image-left .step-copy { left: 462px; }
  .step--image-right .step-visual { left: 436px; }
  .step--image-right .step-copy { left: 8px; }
</style>
</head>
<body>
  <header class="site-header">
    <span class="brand-dot" aria-hidden="true"></span>
    <nav class="main-nav">
      <a href="#" style="left:214px">CATRIDGE REFILLS</a>
      <a href="#" class="is-current" style="left:336px">HOW IT WORKS</a>
      <a href="#" style="left:458px">MY ACCOUNT</a>
      <a href="#" style="left:578px">CHECK OUT</a>
      <a href="#" style="left:668px">ONE YEAR WARRANTY</a>
      <a href="#" style="left:817px">CONTACT</a>
    </nav>
    <div class="brand">
      <span class="brand-mark" aria-hidden="true"></span>
      <span class="brand-name">PEBBLE ARCS</span>
    </div>
  </header>

  <section class="intro">
    <h1>HOW IT WORKS</h1>
    <p>Proin gravida nibh vel velit auctor aliquet. Aenean sollicitudin, lorem quis bibendum auctor, nisi elit conse-<br>quat ipsum, nec sagittis sem nibh id elit. Duis sed odio sit amet nibh vulputate cursus a sit amet mauris.<br>Morbi accumsan ipsum velit. Nam nec tellus a odio tincidunt auctor a ornare odio. Sed non&nbsp; mauris vitae<br>erat consequat auctor eu in elit. Class aptent taciti sociosqu ad litora torquent per conubia nostra, per<br>inceptos himenaeos. Mauris in erat justo. Nullam ac urna eu felis dapibus condimentum sit amet a augue.<br>Sed non neque elit. Sed ut</p>
  </section>

  <section class="step step--image-left" style="top:332px">
    <div class="step-visual" role="img" aria-label="Image for step one">FIRST STEP 1<br>IMAGES</div>
    <div class="step-copy">
      <h2>HOW WORKS 1</h2>
      <p>This is Draftwell's version&nbsp; of Lorem Ipsum. Proin<br>gravida nibh vel velit auctor aliquet. Aenean sol-<br>licitudin, lorem quis bibendum auctor, nisi elit con-<br>sequat ipsum, nec sagittis sem nibh id elit. Duis sed<br>odio sit amet nibh vulputate cursus a sit amet<br>mauris. Morbi accumsan ipsum velit. Nam nec tellus<br>a odio tincidunt auctor a ornare odio. Sed non<br>mauris vitae erat consequat auctor eu in elit.<br>Class aptent taciti sociosqu ad litora torquent</p>
    </div>
  </section>

  <section class="step step--image-right" style="top:627px">
    <div class="step-copy">
      <h2>HOW WORKS 2</h2>
      <p>This is Draftwell's version&nbsp; of Lorem Ipsum. Proin<br>gravida nibh vel velit auctor aliquet. Aenean sol-<br>licitudin, lorem quis bibendum auctor, nisi elit con-<br>sequat ipsum, nec sagittis sem nibh id elit. Duis sed<br>odio sit amet nibh vulputate cursus a sit amet<br>mauris. Morbi accumsan ipsum velit. Nam nec tellus<br>a odio tincidunt auctor a ornare odio. Sed non<br>mauris vitae erat consequat auctor eu in elit.<br>Class aptent taciti sociosqu ad litora torquent</p>
    </div>
    <div class="step-visual" role="img" aria-label="Image for step two">FIRST STEP 2<br>IMAGES</div>
  </section>

  <section class="step step--image-left" style="top:923px">
    <div class="step-visual" role="img" aria-label="Image for step three"></div>
    <div class="step-copy">
      <h2>HOW WORKS 1</h2>
      <p>This is Draftwell's version&nbsp; of Lorem Ipsum. Proin<br>gravida nibh vel velit auctor aliquet. Aenean sol-</p>
    </div>
  </section>
</body>
</html>
```